Plakat für Tanzschule
Zielgruppe
Wir sind eine Tanzschule
Hallo,
ich benötige ein professionelles Design für ein Schild im Format 2 Meter breit × 1 Meter hoch (Querformat), das von einem stark frequentierten Parkplatz aus gut sichtbar ist.
✅ Ziel:
Gestaltung eines aufmerksamkeitsstarken, eleganten und energiegeladenen Werbeschilds
Das Schild soll sofort zeigen, worum es geht (Tanzstile) und zum kostenlosen Schnuppern motivieren
Die Gestaltung soll hochwertig und grafisch modern wirken
Bild / Hintergrund:
Ich habe einen ersten Design-Vorschlag hochgeladen (Screenshot)
⚠️ Ursprünglich hatte ich vor, ein bereits ausgeschnittenes und bearbeitetes Bild zu liefern (z. B. Unreinheiten und Störungen im Bild zu glätten oder zu entfernt und Zähne etwas weißer). Das kann ich jetzt leider doch nicht nachreichen. Daher müsste doch die Bearbeitung des Bildes mit übernommen werden.
✏️ Textinhalte (hierarchisch sortiert):
TANZSCHULE
Salsa · Bachata · Kizomba · Zouk
Jetzt Gratis Schnuppern!
Ritmo y Alma (Markenname)
www.ritmo-y-alma.de
???? Wichtig:
Die wichtigsten Inhalte (Tanzarten & CTA) müssen sofort erfassbar sein
Design bitte auf Fernwirkung, klare Lesbarkeit und modernes visuelles Layout ausrichten
Text in sinnvollen Größenabstufungen und mit sauberer visueller Hierarchie
Unsere eigentliche Hauptfarbe ist #ad194f, bis jetzt habe ich aber noch keine schöne Möglichkeit gefunden, in das aktuelle Design einzuarbeiten.
????️ Endformat & Übergabe:
Bitte das fertige Layout als .afdesign Datei (Affinity Designer) liefern
Optional PSD, EPS

```html
<!DOCTYPE html>
<html lang="de">
<head>
<meta charset="utf-8">
<title>Ritmo y Alma – Tanzschule Plakat</title>
<link rel="stylesheet" href="https://fonts.googleapis.com/css2?family=Montserrat:wght@400;500;700;800&display=swap">
<style>
  :root {
    --brand: #ad194f;
    --brand-bright: #d51f5e;
    --white: #ffffff;
    --ink: #2a2a2a;
    --gold-light: #b08a57;
    --gold-dark: #86602f;
    --stage: #b4b4b4;
  }
  html, body {
    margin: 0;
    padding: 0;
    width: 923px;
    height: 1200px;
    overflow: hidden;
    background: var(--stage);
    font-family: "Montserrat", sans-serif;
  }
  .poster {
    position: absolute;
    left: 32px;
    top: 385px;
    width: 860px;
    height: 430px;
    background: var(--white);
    overflow: hidden;
    box-shadow: 0 10px 24px rgba(0,0,0,0.25);
  }
  .poster__backdrop {
    position: absolute;
    inset: 0;
  }
  .brand {
    position: absolute;
    left: 70px;
    top: 28px;
    display: flex;
    flex-direction: column;
  }
  .brand__name {
    display: flex;
    align-items: center;
    gap: 10px;
    font-size: 30px;
    font-weight: 500;
    color: var(--ink);
    letter-spacing: 0.5px;
  }
  .brand__dot {
    width: 14px;
    height: 14px;
    border-radius: 50%;
    background: var(--brand);
  }
  .brand__tagline {
    margin-top: 4px;
    margin-left: 24px;
    font-size: 11px;
    font-weight: 400;
    color: #555;
  }
  .dancers-photo {
    position: absolute;
    left: 430px;
    top: 30px;
    width: 430px;
    height: 400px;
    background:
      radial-gradient(ellipse at 40% 40%, rgba(226,175,120,0.55), transparent 45%),
      radial-gradient(ellipse at 75% 65%, rgba(104,130,108,0.75), transparent 50%),
      radial-gradient(ellipse at 45% 75%, rgba(236,226,228,0.55), transparent 45%);
    -webkit-mask: linear-gradient(90deg, transparent 0, #000 22%);
            mask: linear-gradient(90deg, transparent 0, #000 22%);
  }
  .offer {
    position: absolute;
    left: 61px;
    top: 158px;
    color: var(--white);
  }
  .offer__kicker {
    font-size: 23px;
    font-weight: 500;
    letter-spacing: 12.5px;
    line-height: 1;
  }
  .offer__styles {
    margin: 8px 0 0;
    font-size: 41px;
    font-weight: 800;
    line-height: 1.02;
    letter-spacing: 0.3px;
  }
  .cta {
    display: inline-block;
    margin-top: 24px;
    width: 386px;
    height: 42px;
    line-height: 42px;
    text-align: center;
    border-radius: 24px;
    border: 2px solid rgba(255,255,255,0.9);
    background: linear-gradient(180deg, var(--gold-light), var(--gold-dark));
    box-shadow: 0 5px 10px rgba(0,0,0,0.3);
    font-size: 20px;
    font-weight: 800;
    color: var(--white);
  }
  .web {
    display: flex;
    align-items: center;
    gap: 10px;
    margin-top: 20px;
    font-size: 24px;
    font-weight: 500;
  }
  .web strong { font-weight: 700; }
  .web__icon { width: 20px; height: 20px; }
</style>
</head>
<body>
  <main class="poster">
    <svg class="poster__backdrop" viewBox="0 0 860 430" width="860" height="430" aria-hidden="true">
      <defs>
        <linearGradient id="bandFill" x1="0" x2="1" y1="0" y2="0">
          <stop offset="0" stop-color="#ad194f"/>
          <stop offset="1" stop-color="#d51f5e"/>
        </linearGradient>
      </defs>
      <path d="M0 78 C 120 150, 250 140, 420 95 C 580 50, 720 10, 860 40 L860 430 L0 430 Z" fill="#9c1646"/>
      <path d="M0 85 C 120 158, 250 148, 420 104 C 580 60, 720 20, 860 50 L860 430 L0 430 Z" fill="url(#bandFill)"/>
    </svg>

    <div class="brand">
      <div class="brand__name"><span>Ritmo y Alma</span><span class="brand__dot"></span></div>
      <div class="brand__tagline">Tanzschule im Herzen Freiburgs</div>
    </div>

    <div class="dancers-photo" role="img" aria-label="Foto: ein lachendes Tanzpaar, sie mit wehendem blondem Haar im weißen Top, er im grünen T-Shirt mit erhobenem Arm"></div>

    <section class="offer">
      <div class="offer__kicker">TANZSCHULE</div>
      <h1 class="offer__styles">SALSA • BACHATA<br>KIZOMBA • ZOUK</h1>
      <div class="cta">JETZT GRATIS SCHNUPPERN!</div>
      <div class="web">
        <svg class="web__icon" viewBox="0 0 20 20" aria-hidden="true">
          <circle cx="10" cy="10" r="10" fill="#fff"/>
          <g fill="none" stroke="#ad194f" stroke-width="1.2">
            <circle cx="10" cy="10" r="5.5"/>
            <ellipse cx="10" cy="10" rx="2.4" ry="5.5"/>
            <line x1="4.5" y1="10" x2="15.5" y2="10"/>
          </g>
        </svg>
        <span>www.<strong>ritmo-y-alma</strong>.de</span>
      </div>
    </section>
  </main>
</body>
</html>
```